Ironvale Holdings Business card

We need a an amazing matte black and gold card! W are a finance investing company so we want something that's eye catching and sleek. We want it to be attractive and sleek and represent money. Heck with would like the letters and lgo to be printed as 24k gold one day. We have the logo added so please use the color scheme with the logo and have that beautifully placed on one side.

Target Market(s)

Investors of all ages

Industry/Entity Type

Financial

Contact Information for Business Card

Black and matte with gold lettering follow logo colrs please.

Font styles to use
Other font styles liked:
• you decide

Colors

Designer to choose colors to be used in the design.

Requirements
Must have
• Matte Black and Gold, logo on one side. job title and name , website, phone number and email address on the other side
Nice to have
• Matte black and crisp finish to attract investors
Should not have
• playful, very professional!

```html
<!DOCTYPE html>
<html lang="en">
<head>
<meta charset="utf-8">
<title>Ironvale Holdings — Business Card</title>
<link rel="stylesheet" href="https://fonts.googleapis.com/css2?family=Open+Sans:wght@400;600&display=swap">
<style>
  :root {
    --backdrop: #d6d7d6;
    --card: #242424;
    --gold: #c9a227;
    --gold-soft: #b8962e;
    --shadow: rgba(0, 0, 0, 0.28);
  }
  * { margin: 0; padding: 0; box-sizing: border-box; }
  html, body {
    width: 1200px;
    height: 900px;
    overflow: hidden;
    background: var(--backdrop);
    font-family: "Open Sans", Arial, sans-serif;
  }
  .stage {
    position: relative;
    width: 1200px;
    height: 900px;
  }
  .card {
    position: absolute;
    width: 520px;
    height: 297px;
    background: var(--card);
    box-shadow: 0 10px 24px var(--shadow), 0 2px 4px rgba(0,0,0,0.2);
  }
  .card--front { left: 90px; top: 140px; }
  .card--back { left: 590px; top: 463px; }

  .wordmark {
    color: var(--gold);
    font-weight: 600;
    text-transform: uppercase;
    letter-spacing: 0.12em;
    white-space: nowrap;
  }
  .card--front .wordmark {
    position: absolute;
    left: 0; right: 0;
    top: 50%;
    transform: translateY(-50%);
    text-align: center;
    font-size: 30px;
  }
  .card--back .wordmark {
    position: absolute;
    left: 34px;
    top: 50%;
    transform: translateY(-50%);
    font-size: 19px;
  }
  .divider {
    position: absolute;
    left: 282px;
    top: 70px;
    width: 1px;
    height: 157px;
    background: var(--gold-soft);
  }
  .contact {
    position: absolute;
    left: 304px;
    top: 72px;
    color: var(--gold-soft);
  }
  .contact__name {
    font-size: 17px;
    font-weight: 600;
    color: var(--gold);
    line-height: 1.2;
  }
  .contact__title {
    font-size: 12px;
    margin-bottom: 18px;
  }
  .contact__list { list-style: none; }
  .contact__item {
    display: flex;
    align-items: center;
    gap: 8px;
    font-size: 12px;
    line-height: 1.75;
  }
  .contact__icon {
    width: 11px;
    height: 11px;
    flex: none;
    fill: none;
    stroke: var(--gold);
    stroke-width: 1.4;
  }
</style>
</head>
<body>
<main class="stage">
  <section class="card card--front" aria-label="Card front">
    <p class="wordmark">Ironvale Holdings</p>
  </section>

  <section class="card card--back" aria-label="Card back">
    <p class="wordmark">Ironvale Holdings</p>
    <div class="divider"></div>
    <div class="contact">
      <p class="contact__name">Daniel Harper</p>
      <p class="contact__title">President</p>
      <ul class="contact__list">
        <li class="contact__item">
          <svg class="contact__icon" viewBox="0 0 12 12" aria-hidden="true">
            <path d="M2.5 1.2 L4.4 1.2 L5.2 3.6 L4 4.5 C4.6 5.9 6.1 7.4 7.5 8 L8.4 6.8 L10.8 7.6 L10.8 9.5 C10.8 10.3 10.1 10.8 9.3 10.8 C5 10.5 1.5 7 1.2 2.7 C1.2 1.9 1.7 1.2 2.5 1.2 Z"/>
          </svg>
          (555) 204-3187
        </li>
        <li class="contact__item">
          <svg class="contact__icon" viewBox="0 0 12 12" aria-hidden="true">
            <rect x="1" y="2.5" width="10" height="7"/>
            <path d="M1 2.5 L6 6.5 L11 2.5"/>
          </svg>
          daniel@ironvaleholdings.com
        </li>
        <li class="contact__item">
          <svg class="contact__icon" viewBox="0 0 12 12" aria-hidden="true">
            <circle cx="6" cy="6" r="4.8"/>
            <ellipse cx="6" cy="6" rx="2" ry="4.8"/>
            <path d="M1.2 6 H10.8"/>
          </svg>
          www.ironvaleholdings.com
        </li>
      </ul>
    </div>
  </section>
</main>
</body>
</html>
```